ebook cover: book 4 in the You Grow Pepper series. Warmth Beyond Fences

I am wanting a striking cover to bring the forth book in a spiritual journey series to an audience ready to meet new characters and get excited again! White backgrounds, red titles (any font), subtitles to introduce a new major character in the series of ten (same fonts please as the original, You Grow Pepper), and one emblematic, slightly mysterious image. Please keep to the same colour tones as the original, but the lead image need not be gray. Let's please try to use the "light flash" that is on the tin can in You Grow Pepper somehow, in your own way. It is meant to signify the other side, or the higher light, or some such inference.

Book details:
Title: Warmth Beyond Fences
Subtitle: Elder Corvanel brings the message
Image: silver hourglass
Author: Mabel Quinlow, Ph.D
Strap quote: "Quinlow is smart, savvy and full of ideas," Harwick Evening Ledger

Please do your best: this one is going in competition of spiritual healers!

Thanks! :)

```html
<!DOCTYPE html>
<html lang="en">
<head>
<meta charset="utf-8">
<title>Warmth Beyond Fences — Mabel Quinlow Ph.D.</title>
<link rel="stylesheet" href="https://fonts.googleapis.com/css2?family=Oranienbaum&family=Open+Sans:wght@600&family=Montserrat:wght@400&display=swap">
<style>
  :root {
    --paper: #ffffff;
    --title-red: #c0141b;
    --ink: #222222;
    --author-grey: #6b6b6b;
    --silver-light: #f4f4f4;
    --silver-mid: #c9c9c9;
    --silver-dark: #8d8d8d;
  }
  html, body {
    margin: 0;
    padding: 0;
    overflow: hidden;
    background: var(--paper);
  }
  .cover {
    position: relative;
    width: 800px;
    height: 1200px;
    background: var(--paper);
    overflow: hidden;
  }
  .strap-quote {
    position: absolute;
    top: 48px;
    left: 0;
    width: 800px;
    text-align: center;
    margin: 0;
    font-family: "Open Sans", sans-serif;
    font-weight: 600;
    font-size: 14px;
    letter-spacing: 0.3px;
    color: var(--ink);
    text-transform: uppercase;
    white-space: nowrap;
  }
  .strap-quote .source {
    font-size: 16px;
  }
  .book-title {
    position: absolute;
    top: 122px;
    left: 0;
    width: 800px;
    margin: 0;
    text-align: center;
    font-family: "Oranienbaum", serif;
    font-weight: 400;
    font-size: 96px;
    line-height: 104px;
    letter-spacing: -0.5px;
    color: var(--title-red);
    text-transform: uppercase;
    white-space: nowrap;
  }
  .book-title span { display: block; }
  .subtitle {
    position: absolute;
    top: 364px;
    left: 0;
    width: 800px;
    margin: 0;
    text-align: center;
    font-family: "Open Sans", sans-serif;
    font-weight: 600;
    font-size: 31px;
    line-height: 50px;
    letter-spacing: 3.5px;
    color: var(--ink);
    text-transform: uppercase;
    white-space: nowrap;
  }
  .subtitle span { display: block; }
  .lead-image {
    position: absolute;
    top: 545px;
    left: 255px;
    width: 292px;
    height: 430px;
  }
  .author {
    position: absolute;
    top: 1072px;
    left: 0;
    width: 800px;
    margin: 0;
    text-align: center;
    font-family: "Montserrat", sans-serif;
    font-weight: 400;
    font-size: 44px;
    letter-spacing: 5px;
    color: var(--author-grey);
    text-transform: uppercase;
    white-space: nowrap;
  }
</style>
</head>
<body>
  <main class="cover">
    <p class="strap-quote">"Quinlow is smart, savvy and full of ideas" - <span class="source">Harwick Evening Ledger</span></p>

    <h1 class="book-title">
      <span>Warmth Beyond</span>
      <span>Fences</span>
    </h1>

    <h2 class="subtitle">
      <span>Elder Corvanel</span>
      <span>Brings the Message</span>
    </h2>

    <svg class="lead-image" role="img" aria-label="Silver hourglass with white sand on a round polished base" viewBox="0 0 292 430">
      <defs>
        <linearGradient id="silverTone" x1="0" y1="0" x2="1" y2="0">
          <stop offset="0" stop-color="var(--silver-dark)"/>
          <stop offset="0.5" stop-color="var(--silver-light)"/>
          <stop offset="1" stop-color="var(--silver-mid)"/>
        </linearGradient>
      </defs>
      <rect x="0" y="0" width="292" height="430" rx="14" fill="url(#silverTone)"/>
    </svg>

    <p class="author">Mabel Quinlow Ph.D.</p>
  </main>
</body>
</html>
```